Bref créative
Brochure for Geriatric Clinic
LumaCrest Residence & Geriatric SPA
Trifold (3 panel) brochure to be designed for a healthcare company specialized in assisted living facilities and geriatric rehabilitation.
We want to see the medical, the infrastructure and the nature rich enviroment aspects of our business in the design.
We want the brochure to communicate that our primary goal is to improve the quality of life for the senior and their families.
Specification of the folder
11" x 8.5"
279.4 mm x 215.9 mm
27.9 cm x 21.6 cm
3.7" x 8.5"
93.0 mm x 215.9 mm
9.3 cm x 21.6 cm
Please refer to our website at www.lumacrest-care.example, we provided a google translate menu at the bottom for the designers convenience. All pictures are free to use in this project.
Health
Personal, elderly, seniors an their families
Lumacrest logo
.ai format
LumaCrest document brief for brochure

```html
<!DOCTYPE html>
<html lang="en">
<head>
<meta charset="utf-8">
<title>LumaCrest Residence &amp; Geriatric SPA – Trifold Brochure</title>
<link rel="stylesheet" href="https://fonts.googleapis.com/css2?family=Cormorant+Garamond:ital,wght@0,500;0,600;1,500&family=Lora:wght@400;600&display=swap">
<style>
:root{
  --stage:#e7e4dc;
  --cream:#f6f1e1;
  --paper:#fbf8ef;
  --gold:#b89b4c;
  --gold-dark:#8a7230;
  --gold-light:#d9c78f;
  --ink:#5b4a28;
  --ink-soft:#7d6c48;
  --leaf:#6f8a4a;
  --sky:#a9c2cf;
  --map:#ece6d3;
}
*{box-sizing:border-box;margin:0;padding:0}
html,body{width:1200px;height:902px;overflow:hidden}
body{background:var(--stage);font-family:"Lora",Georgia,serif;color:var(--ink);position:relative}
.spread{position:absolute;top:215px;width:560px;height:433px;display:grid;grid-template-columns:repeat(3,1fr);box-shadow:0 6px 18px rgba(60,45,20,.25)}
.spread--outside{left:30px;background:var(--paper)}
.spread--inside{left:610px;background:var(--cream)}
.caption{position:absolute;top:668px;width:560px;text-align:center;font-family:"Cormorant Garamond",Georgia,serif;font-size:17px;color:#4a4030}
.caption--outside{left:30px}.caption--inside{left:610px}
.panel{position:relative;padding:16px 13px;overflow:hidden;border-right:1px solid rgba(184,155,76,.25)}
.panel:last-child{border-right:none}
.spread--outside .panel{background:linear-gradient(180deg,var(--paper) 0%,var(--paper) 68%,var(--gold-light) 84%,var(--gold) 100%)}
h2{font-family:"Cormorant Garamond",Georgia,serif;font-weight:600;font-size:17px;color:var(--gold-dark);margin-bottom:6px}
h3{font-family:"Cormorant Garamond",Georgia,serif;font-weight:600;font-size:12px;color:var(--gold-dark);text-transform:uppercase;letter-spacing:.5px;margin:8px 0 4px}
p,li{font-size:7px;line-height:1.5;color:var(--ink)}
p+p{margin-top:5px}
ul{list-style:none}
li{padding-left:8px;position:relative}
li::before{content:"";position:absolute;left:0;top:4px;width:4px;height:4px;background:var(--gold);border-radius:50%}
.photo{border:2px solid #fff;box-shadow:0 1px 3px rgba(0,0,0,.25)}
.photo--garden{background:linear-gradient(160deg,var(--sky),var(--leaf) 55%,#4e6a34)}
.photo--room{background:linear-gradient(160deg,#efe6d2,#c9b489 60%,#9c8553)}
.photo--pool{background:linear-gradient(170deg,var(--sky),#7fb0c2 50%,#d9cfb3)}
.photo--care{background:linear-gradient(160deg,#f1ece2,#cfc6b6 60%,#a89d88)}
.map{height:118px;background:linear-gradient(135deg,var(--map),#f7f3e6);border:1px solid var(--gold-light);margin:4px 0 8px}
.center{text-align:center}
.contact{position:absolute;left:13px;right:13px;bottom:14px;font-size:7px;color:#fff;text-align:center;line-height:1.6}
.contact svg{width:8px;height:8px;vertical-align:-1px;margin-right:3px}
.brand{display:flex;flex-direction:column;align-items:center;margin-top:6px}
.brand__dot{width:34px;height:34px;border-radius:50%;background:var(--gold)}
.brand__name{font-family:"Cormorant Garamond",Georgia,serif;font-weight:600;font-size:26px;color:var(--gold-dark);margin-top:4px}
.brand__address{font-size:6.5px;color:var(--ink-soft);text-align:center;line-height:1.5;margin-top:2px}
.collage{display:grid;grid-template-columns:1fr 1fr;gap:4px;margin-top:12px;height:130px}
.tagline{position:absolute;left:0;right:0;bottom:22px;text-align:center;font-family:"Cormorant Garamond",Georgia,serif;font-style:italic;font-weight:500;font-size:16px;color:#fff}
.inside-photos{display:flex;gap:5px;margin-bottom:6px}
.inside-photos .photo{flex:1;height:62px}
.about-photo{position:absolute;left:13px;right:13px;bottom:16px;height:110px}
</style>
</head>
<body>

<section class="spread spread--outside" aria-label="Outside of brochure: inner flap, back and cover">
  <article class="panel panel--flap">
    <h2>Quality of Life</h2>
    <p>At LumaCrest we care for seniors with warmth, skill and respect. Our team works every day so that each resident feels safe, valued and truly at home.</p>
    <p>Families are part of our care. We share progress, welcome visits and plan each stay together, so loved ones always know what is happening.</p>
    <p>Surrounded by gardens and fresh air, our residence offers calm spaces for rest, gentle exercise and quiet moments with friends.</p>
    <div class="photo photo--garden" role="img" aria-label="Photo of the residence garden with trees and a walking path" style="height:88px;margin-top:10px"></div>
  </article>

  <article class="panel panel--back">
    <h2 class="center">Our Location</h2>
    <div class="map" role="img" aria-label="Street map showing the route to the residence"></div>
    <p class="center">Ten minutes from the city centre, close to the main road and the park.</p>
    <p class="center">Parking is free for visitors and families at all hours.</p>
    <p class="center">Bus lines 12 and 40 stop at our main gate.</p>
    <div class="contact">
      <div><svg viewBox="0 0 10 10"><path d="M5 0a3.5 3.5 0 0 0-3.5 3.5C1.5 6 5 10 5 10s3.5-4 3.5-6.5A3.5 3.5 0 0 0 5 0z" fill="#fff"/></svg>18 Linden Grove Road, Vale Verde</div>
      <div><svg viewBox="0 0 10 10"><path d="M2 0l2 2.5-1 1.2a6 6 0 0 0 3.3 3.3l1.2-1L10 8l-1.5 2C4 10 0 6 0 1.5z" fill="#fff"/></svg>+00 21 5550 1234</div>
      <div>care@lumacrest-care.example</div>
      <div>www.lumacrest-care.example</div>
    </div>
  </article>

  <article class="panel panel--cover">
    <div class="brand">
      <span class="brand__dot" aria-hidden="true"></span>
      <span class="brand__name">LumaCrest</span>
      <span class="brand__address">18 Linden Grove Road<br>Vale Verde · +00 21 5550 1234</span>
    </div>
    <div class="collage">
      <div class="photo photo--garden" role="img" aria-label="Photo of the garden terrace"></div>
      <div class="photo photo--room" role="img" aria-label="Photo of a resident room"></div>
      <div class="photo photo--pool" role="img" aria-label="Photo of the therapy pool"></div>
      <div class="photo photo--garden" role="img" aria-label="Photo of flower beds near the entrance"></div>
    </div>
    <div class="tagline">Residence &amp; Geriatric SPA</div>
  </article>
</section>
<div class="caption caption--outside">Front, back and folded panel</div>

<section class="spread spread--inside" aria-label="Inside panels of brochure">
  <article class="panel">
    <div class="inside-photos">
      <div class="photo photo--room" role="img" aria-label="Photo of a bright resident room"></div>
      <div class="photo photo--garden" role="img" aria-label="Photo of the outdoor lounge"></div>
    </div>
    <h3>Our Services</h3>
    <ul>
      <li>Assisted living, day and night</li>
      <li>Geriatric rehabilitation</li>
      <li>Physiotherapy and gentle exercise</li>
      <li>Nursing care around the clock</li>
      <li>Balanced meals and diet plans</li>
      <li>Memory and social activities</li>
    </ul>
    <h3>Medical Care</h3>
    <ul>
      <li>Regular visits by our physicians</li>
      <li>Medication control and review</li>
      <li>Support after hospital stays</li>
    </ul>
  </article>

  <article class="panel">
    <div class="photo photo--pool" role="img" aria-label="Photo of the indoor therapy pool" style="height:90px;margin-bottom:8px"></div>
    <h3>Infrastructure</h3>
    <p>Spacious rooms, accessible bathrooms and wide halls make daily life easy. Every floor has lifts, call buttons and rest areas.</p>
    <h3>Wellness &amp; SPA</h3>
    <ul>
      <li>Hydrotherapy pool</li>
      <li>Massage and relaxation</li>
      <li>Garden walks and fresh air</li>
      <li>Music, reading and crafts</li>
    </ul>
  </article>

  <article class="panel">
    <h3>About Us</h3>
    <p>LumaCrest was founded to give seniors a home where health care and nature meet. Our aim is simple: a better quality of life for every resident and for the families who trust us.</p>
    <p>Our team of doctors, nurses and therapists shares a calm, caring approach built on years of experience.</p>
    <div class="photo photo--care about-photo" role="img" aria-label="Photo of a caregiver with a resident"></div>
  </article>
</section>
<div class="caption caption--inside">Inside panels</div>

</body>
</html>
```